Norwegian Mobile Home/Cabin Producer Needs Brochure Design

We make and deliver our own brand of mobile homes especially made for Norway and it's weather conditions. We differ from other brands in building quality in regards to a much more solid construction, insulation and choices. We work with our customer from the beginning and build them after their demands and wishes.
We need a brochure that holds us out as top of the line. We deliver mobile homes of all kinds and sizes. Both to the private and professional sector.
For the professional sector, mainly camping sites we want to show, lodges-, sanitary- and kitchen wagoons etc.
So we need a brochure of 14-20 pages in A4 where the double pages can be printed in A3 format.
We have logo (provided). But we need cover as well as back suggestions.
It should start with pages where we can teel who we are and stand for.Piicture(s) and space for some editable text (which we can write in norwegian). The text part can have a transparent background......or not. Give us your best shot. Also a smaller part in the private sector that shows winter time.
We want other pages for the private sector that shows what we deliver and the possibilities of choices.
Pages for the the professional sector.
Pages that show our production. How we transport. And the split construction. Only pictures from this portfolio here. (see fotoskap portfolios)
Take a look at provided pictures and our website www.solvikhytta.no for inspiration.
Here's a FotoSkap link to Pictures to choose from. http://bildelagr.example/K4TQ9P
(Hope it Works, let me know if not)
Our company name in small letters "fjordgrønn hyttebygg" means directly translated "fjordgreen cabin builds".
Looking forward to your suggestions.
Target Market(s)
Private market for vacation mobile homes. Camping sites and similar
Industry/Entity Type
Insulation
Requirements
Must have
- Our logo on the front page. Simple but inviting and professional
Logo and address on the back.

```html
<!DOCTYPE html>
<html lang="no">
<head>
<meta charset="utf-8">
<title>fjordgrønn hyttebygg – brosjyreside</title>
<link href="https://fonts.googleapis.com/css2?family=Lato:wght@300;400&family=Cormorant+Garamond:ital,wght@1,400&display=swap" rel="stylesheet">
<style>
  :root{
    --paper:#ffffff;
    --ink:#3a3a3a;
    --night:#0b0b0c;
    --tagline:#f2f2f2;
    --stone:#d9dadb;
    --kitchen-a:#4a2d1c; --kitchen-b:#a8734a;
    --hall-a:#e9eef3; --hall-b:#6f8fb5;
    --bath-a:#f4f6f8; --bath-b:#2f62a8;
    --yard-a:#7fa85c; --yard-b:#cfd8de;
  }
  *{margin:0;padding:0;box-sizing:border-box}
  html,body{width:900px;height:1200px;overflow:hidden;background:var(--paper)}
  .page{position:relative;width:900px;height:1200px;background:var(--paper);overflow:hidden;font-family:"Lato",sans-serif;color:var(--ink)}
  .block{position:absolute}
  .copy{font-size:13px;font-weight:300;line-height:17px;text-align:justify;hyphens:auto;overflow:hidden}
  .copy p+p{margin-top:17px}
  .photo{position:absolute}
  .photo--kitchen{left:0;top:291px;width:300px;height:204px;background:linear-gradient(135deg,var(--kitchen-a),var(--kitchen-b) 60%,#d9b58a)}
  .photo--hall{left:300px;top:291px;width:315px;height:204px;background:linear-gradient(180deg,var(--hall-a) 55%,var(--hall-b))}
  .photo--bath{left:615px;top:195px;width:285px;height:405px;background:linear-gradient(160deg,var(--bath-a) 50%,var(--bath-b))}
  .photo--yard{left:615px;top:630px;width:285px;height:165px;background:linear-gradient(180deg,var(--yard-b),var(--yard-a))}
  .band{position:absolute;background:var(--night)}
  .band--mid{left:0;top:495px;width:615px;height:135px}
  .band--foot{left:0;top:1000px;width:615px;height:200px;display:flex;flex-direction:column;justify-content:center;align-items:center;gap:22px}
  .panel--stone{position:absolute;left:615px;top:795px;width:285px;height:405px;background:var(--stone)}
  .tagline{font-family:"Cormorant Garamond",serif;font-style:italic;font-size:24px;letter-spacing:2px;color:var(--tagline)}
</style>
</head>
<body>
<main class="page">
  <div class="block copy" style="left:24px;top:10px;width:276px;height:275px">
    <p>Lorem ipsum dolor sit amet, consectetuer adipiscing elit. Nam nibh. Nunc varius facilisis eros. Sed erat. In in velit quis arcu ornare laoreet. Curabitur adipiscing luctus massa. Integer ut purus ac augue commodo commodo. Nunc nec mi eu justo tempor consectetuer. Etiam vitae nisl. In dignissim lacus ut ante. Cras elit lectus, bibendum a, adipiscing vitae, commodo et, dui. Ut tincidunt tortor.</p>
  </div>
  <div class="block copy" style="left:315px;top:10px;width:285px;height:275px">
    <p>tae, commodo et, dui. Ut tincidunt tortor. Donec nonummy, enim in lacinia pulvinar, velit tellus scelerisque augue, ac posuere libero urna eget neque. Cras ipsum. Vestibulum pretium, lectus nec venenatis volutpat, purus lectus ultrices risus, a condimentum risus mi et quam. Pellentesque auctor fringilla neque. Duis eu massa ut lorem iaculis vestibulum.</p>
  </div>
  <div class="block copy" style="left:615px;top:10px;width:279px;height:185px">
    <p>tum. Maecenas facilisis elit sed justo. Quisque volutpat malesuada velit. Fusce auctor metus eu ultricies volputate, sapien nibh faucibus ligula, eget sollicitudin augue risus et dolor. Aenean pellentesque, tortor in cursus mattis, ante diam.</p>
  </div>

  <div class="photo photo--kitchen" role="img" aria-label="Interiør med kjøkken og stue i varme tretoner"></div>
  <div class="photo photo--hall" role="img" aria-label="Lys gang i sanitærvogn med blå flisgulv"></div>
  <div class="photo photo--bath" role="img" aria-label="Baderom med hvite vegger og blå fliser"></div>
  <div class="band band--mid"></div>

  <div class="block copy" style="left:24px;top:645px;width:276px;height:350px">
    <p>Lorem ipsum dolor sit amet, consectetuer adipiscing elit. Nam nibh. Nunc varius facilisis eros. Sed erat. In in velit quis arcu ornare laoreet. Curabitur adipiscing luctus massa. Integer ut purus ac augue commodo commodo. Nunc nec mi eu justo tempor consectetuer. Etiam vitae nisl. In dignissim lacus ut ante. Cras elit lectus, bibendum a, adipiscing vitae, commodo et, dui. Ut tincidunt tortor. Donec nonummy, enim in lacinia pulvinar, velit tellus scelerisque augue, ac posuere libero urna eget neque. Cras ipsum.</p>
  </div>
  <div class="block copy" style="left:315px;top:645px;width:285px;height:350px">
    <p>Vestibulum pretium, lectus nec venenatis volutpat, purus lectus ultrices risus, a condimentum risus mi et quam. Pellentesque auctor fringilla neque. Duis eu massa ut lorem iaculis vestibulum. Maecenas facilisis elit sed justo. Quisque volutpat malesuada velit.</p>
    <p>Nunc at velit quis lectus nonummy eleifend. Curabitur eros. Aenean ligula dolor, gravida auctor, auctor et, suscipit in, erat. Sed malesuada, enim ut congue pharetra, massa elit convallis pede, ornare scelerisque.</p>
  </div>
  <div class="photo photo--yard" role="img" aria-label="Mobilhytte på tomt med bil parkert foran"></div>
  <div class="panel--stone"></div>

  <div class="band band--foot">
    <span class="tagline">We differ from other brands</span>
    <span class="tagline">in building quality in regards to a</span>
  </div>
</main>
</body>
</html>
```